Labels for an activated Charcoal Facial Wash, Scrub and Mask

We need a new label design for a new line of Facial products. The product, falls under our Brand Lumivo and is based on Activated Charcoal. Activated Black Charcoal Facial wash (250ml), Activated Black Charcoal Mask (100gms) and Activated Black Charcoal face scrub (100gms). We would like to see designs that are modern, clean and must communicate natural products.

```html
<!DOCTYPE html>
<html lang="en">
<head>
<meta charset="utf-8">
<title>Lumivo Activated Black Charcoal Facial Wash Label</title>
<link href="https://fonts.googleapis.com/css2?family=Cormorant+Garamond:wght@500&family=Libre+Baskerville:wght@700&family=Satisfy&family=Roboto:wght@400&family=Playfair+Display:wght@500&display=swap" rel="stylesheet">
<style>
  :root {
    --label-white: #f7f7f5;
    --ink: #1f1f1f;
    --ink-soft: #3a3a3a;
    --sage-light: #dedcc4;
    --sage-fade: rgba(222, 220, 196, 0.35);
    --sage-clear: rgba(222, 220, 196, 0);
  }
  * { margin: 0; padding: 0; box-sizing: border-box; }
  html, body { width: 901px; height: 1200px; overflow: hidden; }
  body { background: var(--label-white); }
  .label {
    position: relative;
    width: 901px;
    height: 1200px;
    background: var(--label-white);
    color: var(--ink);
  }
  .art { position: absolute; z-index: 0; }
  .text { position: absolute; z-index: 1; }
  .sprig-art {
    left: 110px;
    top: 90px;
    width: 400px;
    height: 160px;
    border-radius: 50% 50% 45% 55% / 60% 60% 40% 40%;
    background: radial-gradient(ellipse at center, var(--sage-light) 0%, var(--sage-fade) 70%, var(--sage-clear) 100%);
  }
  .leaf-art {
    left: 490px;
    top: 690px;
    width: 390px;
    height: 380px;
    border-radius: 60% 40% 50% 50% / 50% 50% 50% 50%;
    background: radial-gradient(ellipse at 55% 45%, var(--sage-light) 0%, var(--sage-fade) 65%, var(--sage-clear) 100%);
  }
  .brand {
    left: 104px;
    top: 268px;
    font-family: "Cormorant Garamond", serif;
    font-weight: 500;
    font-size: 64px;
    letter-spacing: 0.3em;
    color: var(--ink-soft);
  }
  .product-prefix {
    left: 108px;
    top: 478px;
    font-family: "Satisfy", cursive;
    font-size: 52px;
    line-height: 60px;
    color: var(--ink);
  }
  .product-name {
    left: 104px;
    top: 550px;
    font-family: "Libre Baskerville", serif;
    font-weight: 700;
    font-size: 76px;
    line-height: 92px;
    letter-spacing: -0.01em;
    color: var(--ink);
  }
  .divider {
    left: 108px;
    top: 792px;
    width: 44px;
    height: 5px;
    background: var(--ink);
  }
  .benefits {
    left: 108px;
    top: 815px;
    list-style: none;
    font-family: "Roboto", sans-serif;
    font-size: 29px;
    line-height: 44px;
    text-transform: uppercase;
    color: var(--ink-soft);
  }
  .net-volume {
    left: 0;
    width: 901px;
    top: 1095px;
    text-align: center;
    font-family: "Playfair Display", serif;
    font-weight: 500;
    font-size: 28px;
    color: var(--ink);
  }
</style>
</head>
<body>
  <main class="label">
    <div class="art sprig-art" role="img" aria-label="Line drawing of a small leafy sprig in sage green"></div>
    <div class="art leaf-art" role="img" aria-label="Line drawing of a leafy botanical branch in sage green"></div>
    <div class="text brand">LUMIVO</div>
    <div class="text product-prefix">Activated</div>
    <h1 class="text product-name">Black Charcoal<br>Facial wash</h1>
    <div class="text divider"></div>
    <ul class="text benefits">
      <li>Protect and promote</li>
      <li>Clear skin</li>
      <li>Oil control</li>
    </ul>
    <div class="text net-volume">7 fl oz. ( 250ml )</div>
  </main>
</body>
</html>
```